Bramble Hollow Networks - Electrical

We need flyers for electrical services.
Areas of work include new builds, office fitouts, switchboard upgrades, installation of ceiling fans, powerpoint and downlight upgrades, home theatre and AV systems, all exterior and emergency work. Free quotes
We would like to see designs with the colour Red with a young and modern design. Licence No: 63914K must be included and call Leopold on 0438917062.

Colors
ec1f27

```html
<!DOCTYPE html>
<html lang="en">
<head>
<meta charset="utf-8">
<title>Bramble Hollow Networks – Electrical Services Flyer</title>
<link rel="stylesheet" href="https://fonts.googleapis.com/css2?family=Oswald:wght@500;600&family=Lato:wght@400;700&family=Archivo+Black&display=swap">
<style>
  :root {
    --brand-red: #ec1f27;
    --ink: #111111;
    --paper: #ffffff;
    --backdrop: #3a3a3a;
    --text-dark: #1c1c1c;
  }
  html, body {
    margin: 0;
    width: 1200px;
    height: 1200px;
    overflow: hidden;
    background: var(--backdrop);
  }
  .flyer {
    position: absolute;
    left: 256px;
    top: 118px;
    width: 688px;
    height: 965px;
    display: block;
  }
  .headline { font-family: "Oswald", sans-serif; font-weight: 600; fill: var(--paper); }
  .tagline { font-family: "Archivo Black", sans-serif; fill: var(--paper); }
  .condensed { font-family: "Oswald", sans-serif; font-weight: 500; }
  .body-copy { font-family: "Lato", sans-serif; fill: var(--text-dark); }
  .company-name { font-family: "Lato", sans-serif; font-weight: 700; fill: var(--brand-red); }
  .service-item { font-family: "Lato", sans-serif; font-size: 19px; fill: var(--text-dark); }
  .tick { fill: none; stroke: var(--brand-red); stroke-width: 2.6; stroke-linecap: round; stroke-linejoin: round; }
</style>
</head>
<body>
<svg class="flyer" viewBox="0 0 860 1206" xmlns="http://www.w3.org/2000/svg">
  <defs>
    <linearGradient id="heroTone" x1="0" y1="0" x2="1" y2="1">
      <stop offset="0" stop-color="#d8cfc4"/>
      <stop offset="0.45" stop-color="#9a8b7e"/>
      <stop offset="1" stop-color="#6f6a66"/>
    </linearGradient>
    <linearGradient id="thermalTone" x1="0" y1="0" x2="1" y2="1">
      <stop offset="0" stop-color="#c9ced4"/>
      <stop offset="1" stop-color="#5a6f93"/>
    </linearGradient>
    <linearGradient id="kitchenTone" x1="0" y1="0" x2="1" y2="1">
      <stop offset="0" stop-color="#c8b89f"/>
      <stop offset="1" stop-color="#6b7894"/>
    </linearGradient>
    <linearGradient id="socketTone" x1="0" y1="0" x2="1" y2="1">
      <stop offset="0" stop-color="#eef0f2"/>
      <stop offset="1" stop-color="#b7bcc2"/>
    </linearGradient>
  </defs>

  <rect class="paper" width="860" height="1206" fill="var(--paper)"/>

  <!-- hero photo area -->
  <polygon role="img" aria-label="Electrician in hard hat and overalls inspecting a switchboard cabinet" points="0,0 860,0 860,381 0,611" fill="url(#heroTone)"/>

  <!-- diagonal bands -->
  <polygon class="band-black" points="0,611 860,381 860,470 0,700" fill="var(--ink)"/>
  <polygon class="band-red" points="0,690 860,456 860,611 0,860" fill="var(--brand-red)"/>

  <!-- headline banner -->
  <polygon class="banner-shadow" points="73,590 788,398 788,586 73,781" fill="var(--ink)"/>
  <polygon class="banner" points="91,566 771,379 773,571 91,761" fill="var(--brand-red)"/>
  <g transform="rotate(-15.4 100 700)">
    <text class="headline" x="118" y="668" font-size="84" textLength="640" lengthAdjust="spacingAndGlyphs">ELECTRICAL SERVICES</text>
    <text class="tagline" x="128" y="728" font-size="45" textLength="640" lengthAdjust="spacingAndGlyphs">We Offer Great Services</text>
  </g>

  <!-- white lower area -->
  <polygon class="lower-panel" points="0,856 860,611 860,1206 0,1206" fill="var(--paper)"/>

  <!-- free quotes tab -->
  <polygon class="quotes-tab" points="0,850 140,812 118,1026 0,1030" fill="var(--brand-red)"/>
  <text class="condensed" x="15" y="932" font-size="36" fill="var(--paper)" textLength="62" lengthAdjust="spacingAndGlyphs">FREE</text>
  <text class="condensed" x="15" y="974" font-size="36" fill="var(--paper)" textLength="95" lengthAdjust="spacingAndGlyphs">QUOTES</text>

  <!-- service photos -->
  <polygon role="img" aria-label="Electrician using a thermal camera on a switchboard" points="158,826 373,768 357,930 140,990" fill="url(#thermalTone)"/>
  <polygon role="img" aria-label="Smiling electrician testing wiring with a multimeter in a kitchen" points="396,761 608,704 593,862 373,926" fill="url(#kitchenTone)"/>
  <polygon role="img" aria-label="Hand testing a wall socket with a screwdriver" points="635,694 845,636 828,801 608,861" fill="url(#socketTone)"/>
  <polygon class="accent-bar" points="698,858 860,800 860,834 698,876" fill="var(--ink)"/>
  <polygon class="accent-edge" points="845,710 860,690 860,800 835,808" fill="var(--ink)"/>

  <!-- call to action -->
  <text class="condensed" x="34" y="1073" font-size="45" fill="var(--brand-red)" textLength="298" lengthAdjust="spacingAndGlyphs">CALL LEOPOLD ON</text>
  <g class="phone-icon">
    <circle cx="54" cy="1105" r="20" fill="none" stroke="#8a8a8a" stroke-width="2.5"/>
    <path d="M46,1095 c-3,2 -3,8 2,14 c5,6 11,8 14,5 l2,-3 l-5,-4 l-3,2 c-2,-1 -5,-4 -6,-6 l2,-3 l-4,-5 z" fill="#8a8a8a"/>
  </g>
  <text class="condensed" x="91" y="1123" font-size="48" fill="var(--ink)" textLength="245" lengthAdjust="spacing">0438917062</text>
  <text class="company-name" x="56" y="1157" font-size="19">Bramble Hollow Networks</text>
  <text class="body-copy" x="56" y="1177" font-size="18">Licence No : 63914K</text>

  <!-- intro copy -->
  <text class="body-copy" x="373" y="956" font-size="13.5" textLength="442" lengthAdjust="spacing">Lorem ipsum is placeholder text commonly used in the graphic, print, and</text>
  <text class="body-copy" x="373" y="973" font-size="13.5" textLength="390" lengthAdjust="spacing">publishing industries for previewing layouts and visual mockups.</text>

  <!-- services list -->
  <text class="condensed" x="373" y="1019" font-size="38" fill="var(--ink)" textLength="175" lengthAdjust="spacingAndGlyphs">OUR SERVICES</text>
  <line x1="565" y1="1005" x2="710" y2="1005" stroke="var(--brand-red)" stroke-width="5"/>

  <g class="services-left">
    <path class="tick" d="M375,1046 l4,4 l8,-9"/><text class="service-item" x="397" y="1053">New Builds</text>
    <path class="tick" d="M375,1074 l4,4 l8,-9"/><text class="service-item" x="397" y="1081">Office Fitouts</text>
    <path class="tick" d="M375,1103 l4,4 l8,-9"/><text class="service-item" x="397" y="1110">Switchboard Upgrades</text>
    <path class="tick" d="M375,1131 l4,4 l8,-9"/><text class="service-item" x="397" y="1138">Installation of Ceiling Fans</text>
    <path class="tick" d="M375,1159 l4,4 l8,-9"/><text class="service-item" x="397" y="1166">USB Powerpoints</text>
  </g>
  <g class="services-right">
    <path class="tick" d="M637,1047 l4,4 l8,-9"/><text class="service-item" x="659" y="1054">Downlight Upgrades</text>
    <path class="tick" d="M637,1075 l4,4 l8,-9"/><text class="service-item" x="659" y="1082">Home Theatre</text>
    <path class="tick" d="M637,1103 l4,4 l8,-9"/><text class="service-item" x="659" y="1110">AV Systems</text>
    <path class="tick" d="M637,1131 l4,4 l8,-9"/><text class="service-item" x="659" y="1138">All Exterior</text>
    <path class="tick" d="M637,1159 l4,4 l8,-9"/><text class="service-item" x="659" y="1166">Emergency Work</text>
  </g>

  <!-- footer bar -->
  <rect class="footer-bar" x="0" y="1184" width="860" height="22" fill="var(--ink)"/>
</svg>
</body>
</html>
```